Review/Re-Design Supermarket E-Commerce website

We have launched our Supermarket E-commerce Website but feel it is lacking a modern feel.

Please re-design the current Supermarket E-commerce site, creating a more modern look and feel.

I am looking for design changes to things such as:

- Fonts
- Button shape & Size
- Shapes of boxes
- Layout of drop down menus
- A new shopping cart / button
- The Header (and in particular the use and positioning of the logo)
- Supplying a generic background image (currently berries)

Please do not change the structure of the page. For instance, the category selection will always be on the left, the items will always be displayed in rows of 3 and the shopping cart should be on the right.
Updates

Current site can be found at www.brovanmarket.com.au

Project Deadline Extended
Reason: designs coming in are generally too different from current design. we are looking for less that 10% change to the overall look and feel. one aspect that needs a lot of work is the checkout cart on the right hand side. please checkout http://www2.pelkinfreshmart.com.au/?gclid=QXRP4kdmwnLBHTYEzJuaPGEKtB

Target Market(s)

Consumers buying their weekly grocery shopping online

Industry/Entity Type

Shopping

Number of Pages Required

1 page

Requirements
Must have
• Stick to the branding of the Logo. Which is Red, Blue and White.
• Other colours may be used in small percentages.
Should not have
• Do not change the Structure of the site.

```html
<!DOCTYPE html>
<html lang="en"><head><meta charset="utf-8"><title>Brovan Market – Apples</title>
<link href="https://fonts.googleapis.com/css2?family=Lato:wght@400;700&family=Roboto:wght@400;500;700&display=swap" rel="stylesheet">
<style>
:root{--blue:#1b66b1;--red:#e0262b;--orange:#e8511c;--grey:#e9e9e9;--line:#cfcfcf;--text:#333;--muted:#555;--side:#f6f6f6;--gold:#c9a227}
*{box-sizing:border-box;margin:0;padding:0}
html,body{width:800px;height:1200px;overflow:hidden;background:#fff;font-family:'Lato',sans-serif;color:var(--text)}
.page{position:relative;width:800px;height:1200px}
.abs{position:absolute}
.topbar{left:0;top:0;width:800px;height:34px;background:var(--grey);font-size:11px;font-family:'Roboto',sans-serif}
.topbar span{position:absolute;top:11px;display:flex;align-items:center;gap:5px}
.topbar .reg{color:var(--red)}
.header{left:0;top:34px;width:800px;height:67px;border-bottom:2px solid var(--blue)}
.brand{left:26px;top:20px;font-family:'Roboto',sans-serif;font-weight:700;font-size:22px;color:var(--blue);letter-spacing:.5px;display:flex;align-items:center;gap:8px}
.brand i{display:block;width:14px;height:14px;background:var(--red);border-radius:50%}
.search{left:336px;top:21px;width:265px;height:25px;display:flex}
.search input{flex:1;border:1px solid #ccc;font:11px 'Lato',sans-serif;padding-left:8px;color:#bbb}
.search button{width:61px;border:0;background:#444;color:#fff;font:12px 'Roboto',sans-serif}
.basket{left:662px;top:9px;width:114px;height:49px;border:1px solid #ddd;display:flex;align-items:center;gap:10px;padding-left:10px;font-family:'Roboto',sans-serif;font-size:11px;color:var(--blue);line-height:1.2}
.basket b{font-weight:500}
.sidehead{left:16px;top:101px;width:184px;height:37px;background:var(--blue);color:#fff;font-weight:700;font-size:12px;padding:15px 14px}
.nav{left:200px;top:101px;width:593px;height:37px;border:1px solid #ddd;border-top:0;font-family:'Roboto',sans-serif;font-size:12px;color:#222}
.nav span{position:absolute;top:15px}
.nav .sym{color:var(--blue)}
.sidebar{left:16px;top:138px;width:184px;height:812px;background:var(--side);box-shadow:1px 1px 2px #ddd;list-style:none;padding-top:8px}
.sidebar li{height:24px;font-size:9.5px;padding:6px 0 0 21px;position:relative;color:#333}
.sidebar li::after{content:'>';position:absolute;right:22px;top:6px;color:#999;font-size:8px}
.crumbs{left:214px;top:153px;font-size:11px;color:#666;word-spacing:4px}
.crumbs .here{color:var(--red)}
.card{width:178px;height:262px;border:1px solid var(--line);background:#fff}
.photo{position:absolute;left:14px;top:10px;width:148px;height:134px}
.red{background:radial-gradient(ellipse at 50% 50%,#d22630 0%,#e86a6e 45%,#fff 75%)}
.green{background:radial-gradient(ellipse at 50% 50%,#a9c43a 0%,#cfe08a 45%,#fff 75%)}
.name{position:absolute;top:155px;width:100%;text-align:center;font-family:'Roboto',sans-serif;font-size:11.5px}
.name small{font-family:'Lato',sans-serif;font-size:8.5px;color:var(--muted);margin-left:6px}
.price{position:absolute;top:174px;width:100%;text-align:center;color:var(--red);font-family:'Roboto',sans-serif;font-size:11.5px;font-weight:500}
.qty{position:absolute;left:16px;top:212px;display:flex;align-items:center;gap:10px;font-size:11px}
.qty i{display:block;width:11px;height:11px;border-radius:50%;background:#ddd;border:1px solid #bbb;font-style:normal;font-size:8px;text-align:center;line-height:9px}
.add{position:absolute;left:97px;top:206px;width:76px;height:24px;background:var(--orange);color:#fff;border:0;font:500 12px 'Roboto',sans-serif}
.footer{left:0;top:971px;width:800px;height:229px;background:var(--grey);font-family:'Roboto',sans-serif}
.footer h4{position:absolute;font-weight:500;font-size:12px;color:#333}
.store{position:absolute;top:47px;height:38px;background:#000;color:#fff;font-size:15px;display:flex;align-items:center;justify-content:center}
.links{position:absolute;list-style:none;font-family:'Lato',sans-serif;font-size:9.5px;color:#555}
.links li{height:24px}
.pay{position:absolute;top:155px;font-weight:700;font-size:12px}
.dot{position:absolute;width:24px;height:24px;border-radius:50%}
</style></head><body><div class="page">

<div class="abs topbar">
<span style="left:25px"><svg width="12" height="12" viewBox="0 0 12 12"><path d="M3 1l2 3-1 1.3a7 7 0 003 3L8.5 7l3 2-1 2C5 11 1 7 1 2z" fill="none" stroke="#999"/></svg>1300 555 019</span>
<span style="left:134px"><svg width="8" height="12"><rect x="1" y="1" width="6" height="10" rx="3" fill="#999"/></svg>Click and Collect</span>
<span style="left:248px"><svg width="14" height="10"><rect x="0" y="1" width="9" height="6" fill="#999"/><rect x="9" y="3" width="4" height="4" fill="#999"/><circle cx="3" cy="8.5" r="1.5" fill="#999"/><circle cx="11" cy="8.5" r="1.5" fill="#999"/></svg>Delivery Info</span>
<span style="left:630px">Products</span><span style="left:681px">Login</span><span style="left:718px" class="reg">Register</span>
</div>

<div class="abs header">
<div class="abs brand">Brovan Market<i></i></div>
<div class="abs search"><input value="Search for product"><button>Search</button></div>
<div class="abs basket"><svg width="26" height="22" viewBox="0 0 26 22"><path d="M2 9h22l-3 11H5z" fill="#e0262b"/><path d="M8 9l5-7 5 7" fill="none" stroke="#e0262b" stroke-width="2"/></svg><div>Your Basket<br><b>0 items</b></div></div>
</div>

<div class="abs sidehead">Shop by category</div>
<div class="abs nav"><span style="left:11px"><span class="sym" style="position:static">$</span> Online Special</span><span style="left:118px"><span class="sym" style="position:static">★</span> Favourite</span></div>

<ul class="abs sidebar">
<li>Baby</li><li>Bakery</li><li>Baking needs</li><li>Beverages</li><li>Biscuits</li><li>Breakfast foods</li><li>Canned foods</li><li>Cheese</li><li>Chilled foods</li><li>Chips</li><li>Condiments</li><li>Confectionery</li><li>Cooking needs</li><li>Desserts</li><li>Frozen foods</li><li>Fruit</li><li>Hardware and Outdoor</li><li>Health foods</li><li>Homewares</li><li>Household cleaning</li><li>International foods</li><li>Jams and Spreads</li><li>Laundry</li><li>Meat</li><li>Milk</li><li>Packet food</li><li>Pet care</li><li>Serviced Deli</li><li>Snacks</li><li>Soft drinks</li><li>Tissue products</li><li>Toiletries and Beauty</li><li>Vegetable</li>
</ul>

<div class="abs crumbs">Home &gt;&gt; Fruits &gt;&gt; <span class="here">Apples</span></div>

<div class="abs card" style="left:211px;top:179px"><div class="photo red" role="img" aria-label="Product photo: pile of red apples"></div><div class="name">Apple Red<small>2kg bag</small></div><div class="price">$8.39</div><div class="qty"><i>-</i>1<i>+</i></div><button class="add">ADD</button></div>
<div class="abs card" style="left:406px;top:179px"><div class="photo red" role="img" aria-label="Product photo: pile of red apples"></div><div class="name">Apple Red<small>2kg bag</small></div><div class="price">$8.39</div><div class="qty"><i>-</i>1<i>+</i></div><button class="add">ADD</button></div>
<div class="abs card" style="left:597px;top:179px"><div class="photo red" role="img" aria-label="Product photo: pile of red apples"></div><div class="name">Apple Red<small>2kg bag</small></div><div class="price">$8.39</div><div class="qty"><i>-</i>1<i>+</i></div><button class="add">ADD</button></div>
<div class="abs card" style="left:211px;top:455px"><div class="photo green" role="img" aria-label="Product photo: yellow apples with slices"></div><div class="name">Yellow Apples<small>1.5kg bag</small></div><div class="price">$5.20</div><div class="qty"><i>-</i>1<i>+</i></div><button class="add">ADD</button></div>
<div class="abs card" style="left:406px;top:455px"><div class="photo green" role="img" aria-label="Product photo: yellow apples with slices"></div><div class="name">Yellow Apples<small>1.5kg bag</small></div><div class="price">$5.20</div><div class="qty"><i>-</i>1<i>+</i></div><button class="add">ADD</button></div>
<div class="abs card" style="left:597px;top:455px"><div class="photo green" role="img" aria-label="Product photo: yellow apples with slices"></div><div class="name">Yellow Apples<small>1.5kg bag</small></div><div class="price">$5.20</div><div class="qty"><i>-</i>1<i>+</i></div><button class="add">ADD</button></div>

<div class="abs footer">
<h4 style="left:37px;top:27px">Download our app</h4>
<div class="store" style="left:36px;width:123px">Droid Shelf</div>
<div class="store" style="left:173px;width:128px">Pocket Store</div>
<h4 style="left:33px;top:123px">We accept</h4>
<span class="pay" style="left:36px;color:var(--blue)">Paycard</span>
<span class="pay" style="left:94px;color:var(--red)">Mondocard</span>
<div class="dot" style="left:172px;top:151px;background:var(--gold)"></div>
<h4 style="left:355px;top:27px">Informatinal Links</h4>
<ul class="links" style="left:355px;top:54px"><li>My Account</li><li>My Past Orders</li><li>Online Specials</li><li>Everyday Specials</li><li>About QueueLess</li><li>About Us</li></ul>
<div class="abs" style="left:452px;top:51px;width:1px;height:128px;background:#ccc"></div>
<ul class="links" style="left:489px;top:54px"><li>Delivery</li><li>FAQ</li><li>Privacy Policy</li><li>Terms &amp; Conditions</li><li>End User License Agreement</li></ul>
<h4 style="left:656px;top:29px">Contact us</h4>
<div class="links" style="left:657px;top:49px">1300 555 019</div>
<h4 style="left:659px;top:77px">Socialise</h4>
<div class="dot" style="left:656px;top:93px;background:#3b5998"></div>
<div class="dot" style="left:691px;top:95px;background:#3aa3e3"></div>
<div class="dot" style="left:725px;top:95px;background:#e2553f"></div>
</div>

</div></body></html>
```